Industrial Automation company requires a business card design

Valtrin Automation provides design & build of Automated Equipment for manufacturing industry.
www.valtrinautomation.example
The equipment we design is used for manufacturing in sectors such as medical device, pharmaceutical, aerospace and electronics.
We require a new business card design which incorporates our (New) logo and the key message words:
Automated Equipment:
Design, Build, Control, Test, Support

```html
<!DOCTYPE html>
<html lang="en">
<head>
<meta charset="utf-8">
<title>Valtrin Automation – Business Card</title>
<link rel="stylesheet" href="https://fonts.googleapis.com/css2?family=Roboto:wght@400;500;700&display=swap">
<style>
  :root {
    --green: #0f9447;
    --green-dark: #0b7a3a;
    --black: #1b1b1b;
    --charcoal: #222222;
    --white: #ffffff;
    --grey-text: #3a3a3a;
    --page: #d9dadb;
  }
  * { box-sizing: border-box; margin: 0; padding: 0; }
  html, body {
    width: 1200px; height: 950px; overflow: hidden;
    background: var(--page);
    font-family: "Roboto", Arial, sans-serif;
  }
  .sheet {
    position: relative; width: 1200px; height: 950px;
  }
  .card {
    position: absolute; left: 250px; width: 700px; height: 400px;
    overflow: hidden; border-radius: 4px;
    box-shadow: 0 6px 18px rgba(0,0,0,.25);
  }
  /* Back of card */
  .card-back { top: 50px; background: var(--charcoal); color: var(--white); }
  .back-brand {
    position: absolute; top: 120px; left: 0; right: 0;
    display: flex; align-items: center; justify-content: center; gap: 14px;
  }
  .back-brand .mark { width: 26px; height: 26px; background: var(--green); }
  .back-brand .name { font-weight: 700; font-size: 34px; color: var(--white); letter-spacing: .5px; }
  .back-tagline {
    position: absolute; top: 235px; left: 0; right: 0; text-align: center;
  }
  .back-tagline .headline { font-weight: 700; font-size: 22px; }
  .back-tagline .services { margin-top: 8px; font-size: 19px; font-weight: 400; word-spacing: 2px; }

  /* Front of card */
  .card-front { top: 500px; background: var(--white); }
  .card-front .shapes { position: absolute; inset: 0; }
  .front-brand {
    position: absolute; left: 46px; top: 110px;
    display: flex; align-items: center; gap: 12px;
  }
  .front-brand .mark { width: 22px; height: 22px; border-radius: 50%; background: var(--green); }
  .front-brand .name { font-weight: 700; font-size: 30px; color: var(--green); }
  .person { position: absolute; left: 112px; top: 222px; }
  .person .full-name { font-weight: 700; font-size: 21px; color: var(--green); }
  .person .role { font-size: 16px; color: var(--grey-text); margin-top: 4px; }
  .contact {
    position: absolute; right: 24px; top: 116px;
    list-style: none; text-align: right; color: var(--white);
    font-size: 13px; line-height: 21px;
  }
  .contact li { display: flex; justify-content: flex-end; align-items: center; gap: 7px; white-space: nowrap; }
  .contact .icon { width: 13px; height: 13px; flex: none; }
  .contact .address { margin-bottom: 6px; }
</style>
</head>
<body>
<main class="sheet">

  <section class="card card-back" aria-label="Card back">
    <div class="back-brand">
      <span class="mark"></span>
      <span class="name">Valtrin Automation</span>
    </div>
    <div class="back-tagline">
      <p class="headline">Automated Equipment</p>
      <p class="services">Design &bull; Build &bull; Control &bull; Test &bull; Support</p>
    </div>
  </section>

  <section class="card card-front" aria-label="Card front">
    <svg class="shapes" width="700" height="400" viewBox="0 0 700 400">
      <path d="M385 0 H700 V400 H340 C410 300 440 160 385 0 Z" fill="var(--green)"/>
      <path d="M370 0 C425 160 395 300 325 400 H348 C418 300 448 160 393 0 Z" fill="var(--black)"/>
    </svg>

    <div class="front-brand">
      <span class="mark"></span>
      <span class="name">Valtrin Automation</span>
    </div>

    <div class="person">
      <p class="full-name">Marcus Hale</p>
      <p class="role">President</p>
    </div>

    <ul class="contact">
      <li>4127 Harlow Avenue</li>
      <li class="address">Brookfield, NY 11020
        <svg class="icon" viewBox="0 0 14 14"><path d="M2 5 C2 2 12 2 12 5 L10 6 L9 4.5 H5 L4 6 Z M3 7 H11 L12 12 H2 Z" fill="var(--white)"/></svg>
      </li>
      <li>555 0147 2286
        <svg class="icon" viewBox="0 0 14 14"><rect x="3" y="1" width="8" height="4" fill="var(--white)"/><rect x="1" y="5" width="12" height="6" rx="1" fill="var(--white)"/><rect x="4" y="9" width="6" height="4" fill="var(--green)" stroke="var(--white)"/></svg>
      </li>
      <li>555 0193 4471
        <svg class="icon" viewBox="0 0 14 14"><rect x="4" y="1" width="6" height="12" rx="1" fill="var(--white)"/><rect x="5" y="2.5" width="4" height="7" fill="var(--green)"/></svg>
      </li>
      <li>marcus@valtrinautomation.example
        <svg class="icon" viewBox="0 0 14 14"><rect x="1" y="3" width="12" height="8" fill="var(--white)"/><path d="M1 3 L7 8 L13 3" fill="none" stroke="var(--green)" stroke-width="1.2"/></svg>
      </li>
      <li>www.valtrinautomation.example
        <svg class="icon" viewBox="0 0 14 14"><circle cx="7" cy="7" r="6" fill="var(--white)"/><ellipse cx="7" cy="7" rx="2.5" ry="6" fill="none" stroke="var(--green)"/><path d="M1 7 H13" stroke="var(--green)"/></svg>
      </li>
    </ul>
  </section>

</main>
</body>
</html>
```